Oven Cleaning Business owner needs business card design

Hi there,
Would like for a business card to be designed for myself, the owner of a professional oven cleaning business on the Sunshine Coast.
Would like it to look sleek, and modern-ish. Bit creative is encouraged too.
Include following:
Name/title: Corin ter Haghe, Owner
Phone number: 1300 482 916
Email: info@hearthshinecrew.com.au
Website: www.hearthshinecrew.com.au

```html
<!DOCTYPE html>
<html lang="en">
<head>
<meta charset="utf-8">
<title>Hearthshine Crew – Business Card</title>
<link rel="stylesheet" href="https://fonts.googleapis.com/css2?family=Poppins:ital,wght@0,300;0,400;0,700;0,800;1,400;1,700&display=swap">
<style>
  :root {
    --teal: #52c3ca;
    --ink: #1a1a1a;
    --paper: #ffffff;
    --backdrop: #dcdcdc;
  }
  * { margin: 0; padding: 0; box-sizing: border-box; }
  html, body { width: 1200px; height: 1200px; overflow: hidden; }
  body {
    background: var(--backdrop);
    font-family: "Poppins", sans-serif;
    position: relative;
  }
  .card {
    position: absolute;
    left: 143px;
    width: 914px;
    height: 533px;
    overflow: hidden;
    box-shadow: 0 4px 10px rgba(0,0,0,0.18);
  }
  .card-front { top: 52px; background: var(--paper); }
  .card-back { top: 606px; background: var(--teal); }

  .front-art { position: absolute; inset: 0; }

  .brand {
    position: absolute;
    top: 118px;
    left: 0;
    right: 0;
    display: flex;
    justify-content: center;
    align-items: center;
    gap: 22px;
  }
  .brand-dot {
    width: 60px; height: 60px;
    border-radius: 50%;
    background: var(--teal);
  }
  .brand-name {
    font-weight: 800;
    font-size: 50px;
    letter-spacing: 2px;
    color: var(--ink);
    line-height: 1;
  }

  .holder {
    position: absolute;
    left: 64px;
    top: 340px;
    color: var(--ink);
    font-size: 32px;
    line-height: 1.3;
  }
  .holder-name { font-weight: 700; font-style: italic; }
  .holder-title { font-weight: 400; font-style: italic; }

  .contacts {
    position: absolute;
    right: 58px;
    top: 352px;
    list-style: none;
    color: var(--paper);
    font-weight: 300;
    font-size: 22px;
  }
  .contacts li {
    display: flex;
    justify-content: flex-end;
    align-items: center;
    gap: 16px;
    height: 42px;
  }
  .contacts strong { font-weight: 700; }
  .contacts svg { width: 14px; height: 14px; flex: none; }

  .back-brand {
    position: absolute;
    inset: 0;
    display: flex;
    flex-direction: column;
    justify-content: center;
    align-items: center;
    gap: 26px;
  }
  .back-dot {
    width: 150px; height: 150px;
    border-radius: 50%;
    background: var(--paper);
  }
  .back-name {
    font-weight: 800;
    font-size: 44px;
    letter-spacing: 2px;
    color: var(--paper);
  }
</style>
</head>
<body>
  <section class="card card-front">
    <svg class="front-art" viewBox="0 0 914 533" width="914" height="533" aria-hidden="true">
      <polygon points="504,304 914,304 914,533 314,533" fill="var(--teal)"/>
      <polygon points="482,304 498,304 376,456 360,456" fill="var(--ink)"/>
    </svg>

    <div class="brand">
      <span class="brand-dot"></span>
      <span class="brand-name">HEARTHSHINE CREW</span>
    </div>

    <div class="holder">
      <p class="holder-name">Corin<br>ter Haghe</p>
      <p class="holder-title">Owner</p>
    </div>

    <ul class="contacts">
      <li>1300 482 916
        <svg viewBox="0 0 24 24"><path fill="#fff" d="M6.6 10.8a15 15 0 0 0 6.6 6.6l2.2-2.2a1 1 0 0 1 1-.25 11.4 11.4 0 0 0 3.6.57 1 1 0 0 1 1 1V20a1 1 0 0 1-1 1A17 17 0 0 1 3 4a1 1 0 0 1 1-1h3.5a1 1 0 0 1 1 1c0 1.25.2 2.45.57 3.57a1 1 0 0 1-.25 1z"/></svg>
      </li>
      <li>info@hearthshinecrew.com.au
        <svg viewBox="0 0 24 24"><path fill="#fff" d="M2 5h20v14H2z"/><path d="M2 5l10 8 10-8" fill="none" stroke="#52c3ca" stroke-width="2"/></svg>
      </li>
      <li><span>www.<strong>hearthshinecrew</strong>.com.au</span>
        <svg viewBox="0 0 24 24"><circle cx="12" cy="12" r="10" fill="#fff"/><path d="M2 12h20M12 2c3 3 3 17 0 20M12 2c-3 3-3 17 0 20" fill="none" stroke="#52c3ca" stroke-width="1.6"/></svg>
      </li>
    </ul>
  </section>

  <section class="card card-back">
    <div class="back-brand">
      <span class="back-dot"></span>
      <span class="back-name">HEARTHSHINE CREW</span>
    </div>
  </section>
</body>
</html>
```